Modern HomePage Design for Church

We are looking for a modern homepage design using the sections we put together in the template. The colors we want are blue, black, grey, and white. We do not want use the colors in the logo. Please modify the logo color to match the website color scheme.

Target Market(s)

Church

Industry/Entity Type

Church

Number of Pages Required

1 page

Colors
0293ce
ffffff
474747
9d9d9d

```html
<!DOCTYPE html>
<html lang="en">
<head>
<meta charset="utf-8">
<title>Cedar Hill Church</title>
<link rel="stylesheet" href="https://fonts.googleapis.com/css2?family=Montserrat:wght@400;500;600;700&family=Open+Sans:wght@400;600&display=swap">
<style>
:root{
  --blue:#1a4fa0;
  --blue-dark:#0f2f6b;
  --sky:#0293ce;
  --ink:#111418;
  --charcoal:#1c1e22;
  --grey:#474747;
  --grey-mid:#9d9d9d;
  --grey-light:#e8e8e8;
  --paper:#f2f2f2;
  --white:#ffffff;
}
*{box-sizing:border-box;margin:0;padding:0}
html,body{width:1200px;height:5158px;overflow:hidden}
body{font-family:"Open Sans",Arial,sans-serif;color:var(--grey);background:var(--white);position:relative}
h1,h2,h3,h4,.nav,.btn,.label{font-family:"Montserrat",Arial,sans-serif}
.section{position:absolute;left:0;width:1200px}
.btn{display:inline-block;font-size:14px;font-weight:700;letter-spacing:.5px;text-transform:uppercase;text-decoration:none}
.btn-pill{background:var(--blue);color:var(--white);border-radius:28px;padding:16px 34px}
.btn-outline{border:2px solid var(--blue);color:var(--blue);padding:12px 24px}

/* top bar */
.topbar{top:0;height:34px;background:var(--blue-dark);color:var(--white);font-size:12px;font-family:"Montserrat",sans-serif;font-weight:600;text-transform:uppercase;display:flex;justify-content:space-between;align-items:center;padding:0 100px}
.topbar span::before{content:"";display:inline-block;width:9px;height:9px;border:2px solid var(--white);border-radius:50%;margin-right:8px;vertical-align:-1px}

/* brand: single-line name with one plain circle beside it */
.brand{display:flex;align-items:center;justify-content:center;gap:12px;font-family:"Montserrat",sans-serif;font-weight:500;color:var(--blue);white-space:nowrap}
.brand-dot{flex:none;border-radius:50%;background:currentColor}

/* header */
.header{top:34px;height:162px;background:var(--white)}
.call{position:absolute;left:110px;top:36px;display:flex;gap:14px;align-items:center}
.call .label{font-size:15px;color:var(--blue);font-weight:700;line-height:1.2}
.call .num{font-size:15px;color:var(--grey);font-family:"Montserrat",sans-serif}
.header .brand{position:absolute;left:0;right:0;top:46px;font-size:30px;letter-spacing:1px}
.header .brand-dot{width:22px;height:22px}
.give{position:absolute;right:150px;top:34px;padding:14px 34px;font-size:16px}
.nav{position:absolute;top:114px;font-size:15px;font-weight:600;color:var(--ink);display:flex;gap:34px;text-transform:uppercase}
.nav-left{left:100px}.nav-right{right:100px}

.visitor{top:196px;height:50px;background:var(--paper);text-align:center;line-height:50px;font-size:15px;color:var(--ink)}
.visitor b{font-weight:400;margin-right:34px}

/* hero */
.hero{top:248px;height:640px;background:linear-gradient(100deg,#2a1a10 0%,#8a5526 35%,#d7a86a 60%,#f0e6d6 100%)}
.hero-copy{position:absolute;left:90px;top:170px;color:var(--white)}
.hero-copy .brand{justify-content:flex-start;color:var(--white);font-size:56px;letter-spacing:3px}
.hero-copy .brand-dot{width:40px;height:40px}
.hero-copy p{font-family:"Montserrat",sans-serif;font-size:22px;font-weight:700;margin-top:26px;line-height:1.45;text-transform:uppercase}
.hero-curve{position:absolute;left:0;bottom:-1px;width:1200px;height:110px}

/* about */
.about{top:888px;height:702px;background:var(--paper)}
.about-text{position:absolute;left:96px;top:180px;width:480px}
.about-text .kicker{font-family:"Montserrat",sans-serif;font-size:15px;color:var(--ink);margin-bottom:12px;text-transform:uppercase}
.about-text h2{font-size:25px;color:var(--ink);font-weight:600;line-height:1.45;text-transform:uppercase;margin-bottom:18px}
.about-text p{font-size:14px;line-height:1.75;text-align:justify;color:var(--grey);margin-bottom:26px}
.about-photo{position:absolute;left:600px;top:0;width:600px;height:702px;background:linear-gradient(180deg,#f5f5f5 0%,#d9d9d9 55%,#2b2b2b 100%)}

/* countdown */
.countdown{top:1590px;height:285px;background:var(--charcoal);color:var(--white)}
.countdown h2{position:absolute;left:88px;top:66px;font-size:29px;font-weight:600;text-transform:uppercase;white-space:nowrap}
.countdown .date{position:absolute;left:88px;top:114px;font-family:"Montserrat",sans-serif;font-size:24px}
.countdown p{position:absolute;left:88px;top:160px;width:470px;font-size:14px;line-height:1.75}
.timer{position:absolute;left:600px;top:55px;display:flex;gap:30px}
.timer div{width:100px;height:100px;border-radius:50%;background:var(--blue);text-align:center;font-family:"Montserrat",sans-serif;padding-top:20px;font-size:28px;line-height:1.1}
.timer small{display:block;font-size:22px}
.countdown .btn-pill{position:absolute;left:762px;top:173px;padding:14px 42px}

/* features */
.features{top:1875px;height:422px;background:var(--paper)}
.cards{position:absolute;left:88px;top:84px;display:flex;gap:28px}
.card{width:322px;height:260px;background:var(--white);box-shadow:0 2px 10px rgba(0,0,0,.18);text-align:center;padding-top:34px}
.card svg{width:34px;height:34px}
.card h3{font-size:18px;color:var(--blue);font-weight:700;margin:10px 0 12px;text-transform:uppercase}
.card p{font-size:13px;line-height:1.75;color:var(--grey);padding:0 56px}
.card .more{font-size:12px;color:var(--blue);font-weight:700;font-family:"Montserrat",sans-serif;margin-top:10px;display:block}

/* get involved */
.involved{top:2297px;height:540px;background:var(--charcoal)}
.collage{position:absolute;left:0;top:0;width:602px;height:540px;display:grid;grid-template-columns:repeat(3,1fr);grid-template-rows:repeat(3,1fr)}
.collage div:nth-child(1){background:linear-gradient(135deg,#7a5a3a,#c9b89a)}
.collage div:nth-child(2){background:linear-gradient(135deg,#b33030,#e6d4c4)}
.collage div:nth-child(3){background:linear-gradient(135deg,#9fb0c0,#e0e4e8)}
.collage div:nth-child(4){background:linear-gradient(135deg,#2e2e2e,#8a8a8a)}
.collage div:nth-child(5){background:linear-gradient(135deg,#3a3a3a,#aaaaaa)}
.collage div:nth-child(6){background:linear-gradient(135deg,#1c2a4a,#3f5a8a)}
.collage div:nth-child(7){background:linear-gradient(135deg,#4a2e1a,#a8703a)}
.collage div:nth-child(8){background:linear-gradient(135deg,#d8c8a8,#f5ecd8)}
.collage div:nth-child(9){background:linear-gradient(135deg,#3a2e1a,#c7a55a)}
.involved-text{position:absolute;left:632px;top:94px;width:480px;color:var(--white)}
.involved-text h2{font-size:32px;font-weight:600;text-transform:uppercase;margin-bottom:20px}
.involved-text p{font-size:15px;line-height:1.75;text-align:justify;margin-bottom:26px}

/* post grids */
.posts{background:var(--white)}
.posts h2{text-align:center;font-size:32px;color:var(--blue);font-weight:700;text-transform:uppercase}
.post-row{position:absolute;left:92px;display:flex;gap:14px}
.post{width:332px;position:relative}
.post .thumb{height:190px;position:relative}
.post .stamp{position:absolute;left:10px;bottom:0;background:var(--charcoal);color:var(--white);font-size:11px;padding:6px 12px;font-family:"Montserrat",sans-serif}
.post h3{font-size:16px;font-weight:700;color:var(--blue);margin:22px 0 12px;text-transform:uppercase}
.post p{font-size:12px;line-height:1.7;color:var(--grey)}
.post .more{font-size:12px;color:var(--blue);font-weight:700;font-family:"Montserrat",sans-serif;margin-top:12px;display:block}
.blog{top:2837px;height:585px}
.blog h2{margin-top:70px}
.blog .post-row{top:140px}
.events{top:3938px;height:602px}
.events h2{margin-top:92px}
.events .post-row{top:162px}

/* pastors */
.pastors{top:3422px;height:516px;background:var(--ink);color:var(--white)}
.pastors h2{position:absolute;top:96px;font-size:30px;font-weight:500;text-transform:uppercase}
.pastors-title{left:88px}
.podcast-title{left:804px}
.pastor-photo{position:absolute;left:90px;top:182px;width:210px;height:242px;background:linear-gradient(160deg,#9a8a78,#3d3a36)}
.pastor-copy{position:absolute;left:338px;top:180px;width:420px}
.pastor-copy h3{font-size:30px;font-weight:700;text-transform:uppercase;margin-bottom:12px}
.pastor-copy p{font-size:15px;line-height:1.65;margin-bottom:22px}
.podcast{position:absolute;left:804px;top:186px;list-style:none}
.podcast li{display:flex;gap:14px;align-items:center;font-size:12px;line-height:1.6;margin-bottom:20px;width:340px}
.podcast .ico{flex:none;width:40px;height:40px;border-radius:50%;background:var(--white);display:flex;align-items:center;justify-content:center}

/* footer */
.footer{top:4540px;height:618px;background:var(--ink);color:var(--white);text-align:center}
.footer-curve{position:absolute;left:0;top:0;width:1200px;height:110px}
.footer .brand{position:absolute;left:0;right:0;top:170px;color:var(--white);font-size:46px;letter-spacing:3px}
.footer .brand-dot{width:32px;height:32px}
.contacts{position:absolute;left:150px;top:326px;width:900px;display:flex;justify-content:space-between}
.contact{width:300px;font-size:16px;line-height:1.55}
.contact .circle{width:84px;height:84px;border-radius:50%;background:var(--blue);margin:0 auto 18px;display:flex;align-items:center;justify-content:center}
.socials{position:absolute;left:0;right:0;top:515px;display:flex;justify-content:center;gap:8px}
.socials span{width:26px;height:26px;border:2px solid var(--white);border-radius:50%}
.footer-links{position:absolute;left:0;right:0;top:556px;font-size:15px;font-weight:600;font-family:"Montserrat",sans-serif}
.footer-links span{margin:0 10px}
.copyright{position:absolute;left:0;right:0;top:590px;font-size:13px;color:var(--grey-light)}
</style>
</head>
<body>

<div class="section topbar"><span>Sunday Workshop 10:15</span><span>Sunday School 09:00</span></div>

<header class="section header">
  <div class="call">
    <svg width="34" height="34" viewBox="0 0 34 34"><circle cx="17" cy="17" r="15" fill="none" stroke="#1a4fa0" stroke-width="2"/><path d="M12 10c1-1 2-1 3 0l2 3c.5 1 0 2-1 2.5 1 2 2 3 4 4 .5-1 1.5-1.5 2.5-1l3 2c1 1 1 2 0 3-2 2-5 1-8-2s-6-7-5.5-11z" fill="#1a4fa0"/></svg>
    <div><div class="label">SUPPORT CALL US</div><div class="num">888 888 8888</div></div>
  </div>
  <div class="brand"><span class="brand-dot"></span>CEDAR HILL CHURCH</div>
  <a class="btn btn-pill give">Give Online</a>
  <nav class="nav nav-left"><span>Home</span><span>Team</span><span>Features</span><span>Events</span></nav>
  <nav class="nav nav-right"><span>Sermons</span><span>Contact Us</span><span>Our Blog</span></nav>
</header>

<div class="section visitor"><b>First Time Visitor?...</b> Find Out How, where and when we worship, we hope to see you soon!!</div>

<section class="section hero" role="img" aria-label="Congregation seated in wooden church pews">
  <div class="hero-copy">
    <div class="brand"><span class="brand-dot"></span>CEDAR HILL CHURCH</div>
    <p>Sed ut perspiciatis unde omnis iste<br>natus error sit voluptatem</p>
  </div>
  <svg class="hero-curve" viewBox="0 0 1200 110" preserveAspectRatio="none">
    <path d="M0 20 Q600 130 1200 20 L1200 110 L0 110Z" fill="#f2f2f2"/>
    <path d="M0 20 Q600 125 1200 20" fill="none" stroke="#1a4fa0" stroke-width="8"/>
    <path d="M0 32 Q600 122 1200 32" fill="none" stroke="#0f2f6b" stroke-width="3"/>
  </svg>
</section>

<section class="section about">
  <div class="about-text">
    <div class="kicker">About Us</div>
    <h2>Welcome to Cedar Hill<br>Church</h2>
    <p>Sed ut perspiciatis unde omnis iste natus error sit voluptatem accusantium doloremque laudantium, totam rem aperiam, eaque ipsa quae ab illo inventore veritatis et quasi architecto beatae vitae dicta sunt explicabo. Nemo enim ipsam voluptatem quia voluptas sit aspernatur aut odit aut fugit, sed quia consequuntur magni dolores eos qui ratione voluptatem sequi nesciunt.</p>
    <a class="btn btn-outline">Read More</a>
  </div>
  <div class="about-photo" role="img" aria-label="Portrait of the church pastor and his wife"></div>
</section>

<section class="section countdown">
  <h2>Church Leaders Meeting</h2>
  <div class="date">MARCH 12, 2019</div>
  <p>Sed ut perspiciatis unde omnis iste natus error sit voluptatem accusantium doloremque laudantium,</p>
  <div class="timer">
    <div>06<small>Days</small></div>
    <div>15<small>Hours</small></div>
    <div>28<small>Mins</small></div>
    <div>16<small>Sec</small></div>
  </div>
  <a class="btn btn-pill">Read More</a>
</section>

<section class="section features">
  <div class="cards">
    <div class="card">
      <svg viewBox="0 0 34 34"><path d="M17 30 4 17a7 7 0 0 1 13-9 7 7 0 0 1 13 9z" fill="#1a4fa0"/><path d="M6 17h7l2-4 3 8 2-4h8" fill="none" stroke="#fff" stroke-width="2"/></svg>
      <h3>What We Belive</h3>
      <p>Sed ut perspiciatis unde omnis iste natus error sit voluptatem accusantium doloremque laudantium</p>
      <span class="more">Read More →</span>
    </div>
    <div class="card">
      <svg viewBox="0 0 34 34"><circle cx="17" cy="17" r="14" fill="none" stroke="#1a4fa0" stroke-width="3"/><path d="M17 9v9l6 4" fill="none" stroke="#1a4fa0" stroke-width="3"/></svg>
      <h3>Services &amp; Location</h3>
      <p>Sed ut perspiciatis unde omnis iste natus error sit voluptatem accusantium doloremque laudantium</p>
      <span class="more">Read More →</span>
    </div>
    <div class="card">
      <svg viewBox="0 0 34 34"><circle cx="17" cy="9" r="6" fill="#1a4fa0"/><path d="M2 24h10l6 3 10-6c2-1 4 1 2 3l-11 7H2z" fill="#1a4fa0"/></svg>
      <h3>Giving Online</h3>
      <p>Sed ut perspiciatis unde omnis iste natus error sit voluptatem accusantium doloremque laudantium</p>
      <span class="more">Read More →</span>
    </div>
  </div>
</section>

<section class="section involved">
  <div class="collage" role="img" aria-label="Collage of church buildings, worship gatherings and congregation moments">
    <div></div><div></div><div></div><div></div><div></div><div></div><div></div><div></div><div></div>
  </div>
  <div class="involved-text">
    <h2>Get Involved</h2>
    <p>Sed ut perspiciatis unde omnis iste natus error sit voluptatem accusantium doloremque laudantium, totam rem aperiam, eaque ipsa quae ab illo inventore veritatis et quasi architecto beatae vitae dicta sunt explicabo. Nemo enim ipsam voluptatem quia voluptas sit aspernatur aut odit aut fugit, sed quia consequuntur magni dolores eos qui ratione voluptatem sequi nesciunt.</p>
    <a class="btn btn-pill">Read More</a>
  </div>
</section>

<section class="section posts blog">
  <h2>Our Blog</h2>
  <div class="post-row">
    <article class="post">
      <div class="thumb" role="img" aria-label="Worshippers in prayer" style="background:linear-gradient(135deg,#3a2a1a,#9a7a5a)"><span class="stamp">Oct 27 2018</span></div>
      <h3>Sed ut perspiciatis und</h3>
      <p>Sed ut perspiciatis unde omnis iste natus error sit voluptatem accusantium doloremque laudantium, totam rem aperiam, eaque ipsa quae ab illo</p>
      <span class="more">Read More</span>
    </article>
    <article class="post">
      <div class="thumb" role="img" aria-label="Worship concert with stage lights" style="background:linear-gradient(135deg,#5a0a1a,#e03a4a)"><span class="stamp">Oct 27 2018</span></div>
      <h3>Sed ut perspiciatis und</h3>
      <p>Sed ut perspiciatis unde omnis iste natus error sit voluptatem accusantium doloremque laudantium, totam rem aperiam, eaque ipsa quae ab illo</p>
      <span class="more">Read More</span>
    </article>
    <article class="post">
      <div class="thumb" role="img" aria-label="Congregation raising hands in worship" style="background:linear-gradient(135deg,#6a1a1a,#d8a070)"><span class="stamp">Oct 27 2018</span></div>
      <h3>Sed ut perspiciatis und</h3>
      <p>Sed ut perspiciatis unde omnis iste natus error sit voluptatem accusantium doloremque laudantium, totam rem aperiam, eaque ipsa quae ab illo</p>
      <span class="more">Read More</span>
    </article>
  </div>
</section>

<section class="section pastors">
  <h2 class="pastors-title">Pastors</h2>
  <div class="pastor-photo" role="img" aria-label="Portrait of the lead pastor"></div>
  <div class="pastor-copy">
    <h3>Sed ut perspiciatis</h3>
    <p>Sed ut perspiciatis unde omnis iste natus error sit voluptatem accusantium doloremque laudantium, totam rem aperiam, eaque ipsa quae ab illo inventore veritatis et quasi architecto beatae vitae esciunt.</p>
    <a class="btn btn-pill">Read More</a>
  </div>
  <h2 class="podcast-title">Podcast</h2>
  <ul class="podcast">
    <li><span class="ico"><svg width="18" height="18" viewBox="0 0 18 18"><rect x="6" y="1" width="6" height="10" rx="3" fill="#111418"/><path d="M3 8a6 6 0 0 0 12 0M9 14v3" fill="none" stroke="#111418" stroke-width="2"/></svg></span>Sed ut perspiciatis unde omnis iste natus error sit voluptatem accusantium</li>
    <li><span class="ico"><svg width="18" height="18" viewBox="0 0 18 18"><rect x="6" y="1" width="6" height="10" rx="3" fill="#111418"/><path d="M3 8a6 6 0 0 0 12 0M9 14v3" fill="none" stroke="#111418" stroke-width="2"/></svg></span>Sed ut perspiciatis unde omnis iste natus error sit voluptatem accusantium</li>
    <li><span class="ico"><svg width="18" height="18" viewBox="0 0 18 18"><rect x="6" y="1" width="6" height="10" rx="3" fill="#111418"/><path d="M3 8a6 6 0 0 0 12 0M9 14v3" fill="none" stroke="#111418" stroke-width="2"/></svg></span>Sed ut perspiciatis unde omnis iste natus error sit voluptatem accusantium</li>
    <li><span class="ico"><svg width="18" height="18" viewBox="0 0 18 18"><rect x="6" y="1" width="6" height="10" rx="3" fill="#111418"/><path d="M3 8a6 6 0 0 0 12 0M9 14v3" fill="none" stroke="#111418" stroke-width="2"/></svg></span>Sed ut perspiciatis unde omnis iste natus error sit voluptatem accusantium</li>
  </ul>
</section>

<section class="section posts events">
  <h2>Upcoming Events</h2>
  <div class="post-row">
    <article class="post">
      <div class="thumb" role="img" aria-label="Church choir in white robes" style="background:linear-gradient(135deg,#c8b8a0,#f0e8dc)"><span class="stamp">Oct 27 2018</span></div>
      <h3>Sed ut perspiciatis und</h3>
      <p>Sed ut perspiciatis unde omnis iste natus error sit voluptatem accusantium doloremque laudantium, totam rem aperiam, eaque ipsa quae ab illo</p>
      <span class="more">Read More</span>
    </article>
    <article class="post">
      <div class="thumb" role="img" aria-label="Hands folded in prayer" style="background:linear-gradient(135deg,#3a2a20,#b89070)"><span class="stamp">Oct 27 2018</span></div>
      <h3>Sed ut perspiciatis und</h3>
      <p>Sed ut perspiciatis unde omnis iste natus error sit voluptatem accusantium doloremque laudantium, totam rem aperiam, eaque ipsa quae ab illo</p>
      <span class="more">Read More</span>
    </article>
    <article class="post">
      <div class="thumb" role="img" aria-label="Crosses on a hill at sunset" style="background:linear-gradient(135deg,#2a2a1a,#c8b070)"><span class="stamp">Oct 27 2018</span></div>
      <h3>Sed ut perspiciatis und</h3>
      <p>Sed ut perspiciatis unde omnis iste natus error sit voluptatem accusantium doloremque laudantium, totam rem aperiam, eaque ipsa quae ab illo</p>
      <span class="more">Read More</span>
    </article>
  </div>
</section>

<footer class="section footer">
  <svg class="footer-curve" viewBox="0 0 1200 110" preserveAspectRatio="none">
    <path d="M0 0 H1200 V40 Q600 -40 0 40Z" fill="#ffffff"/>
    <path d="M0 40 Q600 -40 1200 40" fill="none" stroke="#1a4fa0" stroke-width="8"/>
    <path d="M0 52 Q600 -28 1200 52" fill="none" stroke="#0f2f6b" stroke-width="3"/>
  </svg>
  <div class="brand"><span class="brand-dot"></span>CEDAR HILL CHURCH</div>
  <div class="contacts">
    <div class="contact">
      <div class="circle"><svg width="36" height="36" viewBox="0 0 36 36"><path d="M18 33s-10-11-10-18a10 10 0 0 1 20 0c0 7-10 18-10 18z" fill="none" stroke="#fff" stroke-width="2.5"/><circle cx="18" cy="15" r="4" fill="none" stroke="#fff" stroke-width="2.5"/></svg></div>
      1420 Harbor Lane<br>Riverton WA 98000
    </div>
    <div class="contact">
      <div class="circle"><svg width="36" height="36" viewBox="0 0 36 36"><path d="M10 5c2-2 4-1 5 1l2 5c.5 1.5-.5 3-2 3.5 1.5 3.5 3.5 5.5 7 7 .5-1.5 2-2.5 3.5-2l5 2c2 1 3 3 1 5-4 4-10 2-16-4S6 9 10 5z" fill="none" stroke="#fff" stroke-width="2.5"/></svg></div>
      Phone:<br>888 888 8888
    </div>
    <div class="contact">
      <div class="circle"><svg width="38" height="30" viewBox="0 0 38 30"><rect x="2" y="3" width="34" height="24" fill="none" stroke="#fff" stroke-width="2.5"/><path d="M2 3l17 14L36 3" fill="none" stroke="#fff" stroke-width="2.5"/></svg></div>
      Email:<br>info@company.com
    </div>
  </div>
  <div class="socials"><span></span><span></span><span></span><span></span></div>
  <div class="footer-links"><span>Home</span>|<span>About Us</span>|<span>Ministries</span>|<span>Small Groups</span>|<span>Current Events</span>|<span>Contact Us</span></div>
  <div class="copyright">© 2019 Company Name. All right reserved</div>
</footer>

</body>
</html>
```